Ferrowave.com website design

I need a basic website for www.ferrowave.com. Ferro Wave has been hosting websites since 2002 via partnership arrangement with Stackhollow.com and Namequarry.com. We do not do any design, only hosting for small companies and nonprofits. We are referring people to PixelGuild and others to get their websites developed. Our website and pricing does not change often, but I need to be able to easily update the pricing and contact page.

Target Market(s)

Small company and non profit organizations

Industry/Entity Type

Utility

Coding

Coded - Design and coding required

Number of Pages Required

5+ page

Colors

Designer to choose colors to be used in the design.

Requirements
Must have
• Wordsmith format for easy content management. The logo attached. Contact us page with the following: Phone and fax are the same number: 888.514.2973. Email address is myferrowave@mailnest.example. Mailing address is 4819 E. Tolliver Bend #317, Holloway Ridge, AR 72190.
Nice to have
• Some kind of badge or tag line on the home page that celebrates our 15th year of hosting without a single hosting without any downtime. We are are 15 year partners with Stackhollow.com and Namequarry.com. Website Design tab needs to reference PixelGuild or others for all their website design needs. We provide no design or updating services. We will provide the developers FTP access to our dedicated Linux server. We do not provide email services other than redirects to their proprietary email or gmail, yahoo, etc. Needs a services and pricing tab. We provide domain registration services via our partnership with Namequarry.com. We will want a way for them to submit a suggested domain name for us to verify if available. I might be able to get a link from Namequarry.com to our account for you to include on that tab REGISTER DOMAIN. The tab buttons can be: WHO WE ARE, WHAT WE DO, WHEN YOU NEED US, WHERE TO REACH US. Maybe consider making the WHO, WHAT, WHEN and WHERE a dark blue color the rest of the text different color just so they stand out
Should not have
• A lot of animation that takes a long time to open. Clean and simple website.

```html
<!DOCTYPE html>
<html lang="en">
<head>
<meta charset="utf-8">
<title>Ferro Wave – Website Hosting</title>
<link href="https://fonts.googleapis.com/css2?family=Montserrat:wght@400;600;700&family=Open+Sans:wght@400;600;700&display=swap" rel="stylesheet">
<style>
:root{
  --blue:#2f86cf;
  --blue-dark:#1d4f86;
  --navy:#16314f;
  --ink:#222a33;
  --muted:#6b7178;
  --line:#d9dde2;
  --grey-bg:#ececef;
  --white:#ffffff;
}
*{box-sizing:border-box;margin:0;padding:0}
html,body{width:1200px;height:3285px;overflow:hidden;background:var(--white)}
body{font-family:"Open Sans",Arial,sans-serif;color:var(--ink);position:relative}
.wrap{width:940px;margin:0 auto;position:relative}
svg{display:block}

/* header */
.site-header{height:153px;position:relative}
.brand{position:absolute;left:130px;top:24px;display:flex;align-items:center;gap:12px}
.brand-mark{width:40px;height:40px;background:var(--blue)}
.brand-name{font-family:"Montserrat",sans-serif;font-weight:700;font-size:30px;color:var(--navy);letter-spacing:.5px}
.brand-sub{position:absolute;left:182px;top:88px;font-size:11px;letter-spacing:3px;color:var(--blue);font-weight:600}
.contacts{position:absolute;left:448px;top:30px;display:flex;gap:40px;white-space:nowrap}
.contact{display:flex;align-items:center;gap:14px;font-size:13px;line-height:1.4;white-space:nowrap}
.contact small{display:block;color:var(--blue);font-size:11px}
.ring{width:34px;height:34px;border:1px solid var(--line);border-radius:50%;display:flex;align-items:center;justify-content:center;flex:none}
.addr{font-size:11.5px}
.main-nav{position:absolute;left:436px;top:108px;display:flex;gap:12px;font-family:"Montserrat",sans-serif;font-size:12px;font-weight:600;color:var(--navy)}
.main-nav a{color:var(--navy);text-decoration:none;padding:6px 14px}
.main-nav a.active{background:var(--blue);color:var(--white)}

/* hero */
.hero{height:530px;position:relative;background:linear-gradient(90deg,#15233f 0%,#3b5f99 35%,#8fa9d1 50%,#3b5f99 65%,#15233f 100%)}
.hero-tag{position:absolute;left:668px;top:147px;width:372px;height:208px;background:rgba(47,134,207,.92);color:var(--white);text-align:center;font-size:27px;line-height:48px;padding-top:30px}
.hero-tag strong{font-weight:700}
.dots{position:absolute;left:0;right:0;top:470px;display:flex;justify-content:center;gap:22px}
.dots span{width:10px;height:10px;border-radius:50%;background:var(--white)}
.dots span.on{background:transparent;border:2px solid var(--white);width:12px;height:12px;margin-top:-1px}

/* section headings */
.section-title{font-family:"Montserrat",sans-serif;font-weight:600;font-size:27px;color:var(--blue);text-align:center;letter-spacing:.5px}
.section-rule{width:72px;height:2px;background:var(--line);margin:22px auto 0}

/* plans */
.plans{height:543px;padding-top:56px}
.plan-row{display:flex;gap:32px;margin-top:54px}
.plan{width:292px;height:306px;border:1px solid #e2e5e8;box-shadow:0 0 18px rgba(0,0,0,.08);text-align:center;padding-top:30px}
.plan h3{font-family:"Open Sans",sans-serif;font-weight:700;font-size:17px;color:var(--navy)}
.plan p{font-size:11px;color:var(--muted);margin-top:6px}
.price{width:184px;height:114px;margin:26px auto 0;background:var(--blue);color:var(--white);padding-top:20px}
.price small{font-size:11px;letter-spacing:3px;font-weight:600}
.price div{font-size:32px;font-weight:600;margin-top:14px}
.price div span{font-size:13px;font-weight:400}
.btn{display:block;width:214px;height:55px;margin:0 auto;border:2px solid var(--blue);background:var(--white);color:var(--blue);font-family:"Montserrat",sans-serif;font-weight:600;font-size:15px;line-height:51px}

/* features */
.features{height:653px;background:var(--grey-bg);padding-top:54px}
.feature-grid{display:grid;grid-template-columns:340px 366px 234px;row-gap:58px;margin-top:60px}
.feature h4{font-family:"Open Sans",sans-serif;font-size:13px;font-weight:700;color:var(--navy);margin-top:18px}
.feature p{font-size:11.5px;color:var(--muted);line-height:22px;margin-top:10px;width:234px}

/* why */
.why{height:504px;padding-top:74px}
.why-grid{display:grid;grid-template-columns:repeat(3,1fr);margin-top:66px;text-align:center}
.why-item svg{margin:0 auto;height:64px}
.why-item h4{font-family:"Open Sans",sans-serif;font-weight:700;font-size:14px;color:var(--navy);margin-top:30px}
.why-item p{font-size:11.5px;color:var(--muted);line-height:22px;width:226px;margin:18px auto 0}

/* advisors */
.advisors{height:453px;background:var(--grey-bg);padding-top:60px}
.advisor-row{display:flex;gap:31px;margin:60px 0 0 40px}
.advisor{width:416px;height:202px;background:var(--white);box-shadow:0 0 14px rgba(0,0,0,.06);display:flex;gap:26px;padding:28px 0 0 24px}
.advisor .photo{width:100px;height:142px;flex:none}
.advisor h4{font-family:"Open Sans",sans-serif;font-weight:700;font-size:12.5px;color:var(--navy);line-height:22px;width:250px}
.advisor p{font-size:11.5px;color:var(--muted);line-height:22px;margin-top:8px;width:250px}
.advisor a{display:block;font-size:10px;font-weight:700;color:var(--blue);text-decoration:none;margin-top:10px}
.arrow{position:absolute;top:160px}

/* contact strip */
.reach{height:110px;border-bottom:1px solid var(--line);position:relative}
.follow{position:absolute;left:0;top:46px;display:flex;align-items:center;gap:6px;font-family:"Montserrat",sans-serif;font-weight:700;font-size:11px;color:var(--navy)}
.follow b{margin-right:14px}
.follow span{width:18px;height:18px;display:block}
.reach .contacts{left:290px;top:34px;gap:40px}

/* footer */
.site-footer{height:251px;position:relative}
.footer-brand{position:absolute;left:0;top:58px;display:flex;align-items:center;gap:12px}
.footer-brand .brand-mark{width:46px;height:46px}
.footer-brand .brand-name{font-size:32px}
.footer-cols{position:absolute;left:368px;top:50px;display:grid;grid-template-columns:241px 245px 160px}
.footer-cols h5{font-family:"Montserrat",sans-serif;font-size:11px;font-weight:700;color:var(--blue-dark);margin-bottom:16px}
.footer-cols li{list-style:none;font-size:11px;line-height:21px;color:var(--ink)}
.bottom-bar{height:88px;border-top:1px solid var(--line);font-size:11px;color:var(--ink)}
.bottom-bar .wrap{display:flex;justify-content:space-between;padding-top:38px}
</style>
</head>
<body>

<header class="site-header">
  <div class="brand"><span class="brand-mark"></span><span class="brand-name">FERRO WAVE</span></div>
  <div class="brand-sub">WEBSITE HOSTING</div>
  <div class="contacts">
    <div class="contact"><span class="ring"><svg width="14" height="10" viewBox="0 0 14 10"><rect width="14" height="10" rx="1" fill="#2f86cf"/><path d="M0 1l7 5 7-5" stroke="#fff" fill="none"/></svg></span><div><small>Email</small>myferrowave@mailnest.example</div></div>
    <div class="contact"><span class="ring"><svg width="14" height="14" viewBox="0 0 24 24"><path fill="#2f86cf" d="M6.6 10.8a15 15 0 006.6 6.6l2.2-2.2c.3-.3.7-.4 1-.2 1.1.4 2.3.6 3.6.6.6 0 1 .4 1 1V20c0 .6-.4 1-1 1A17 17 0 013 4c0-.6.4-1 1-1h3.5c.6 0 1 .4 1 1 0 1.3.2 2.5.6 3.6.1.3 0 .7-.2 1z"/></svg></span><div><small>CALL</small><span style="font-size:15px">888.514.2973</span></div></div>
    <div class="contact"><span class="ring"><svg width="12" height="16" viewBox="0 0 12 16"><path fill="#2f86cf" d="M6 0a6 6 0 00-6 6c0 4.5 6 10 6 10s6-5.5 6-10a6 6 0 00-6-6zm0 8.2A2.2 2.2 0 116 3.8a2.2 2.2 0 010 4.4z"/></svg></span><div class="addr">4819 E. Tolliver Bend #317,<br>Holloway Ridge, AR 72190</div></div>
  </div>
  <nav class="main-nav">
    <a class="active" href="#">HOME</a><a href="#">WHO WE ARE</a><a href="#">WHAT WE DO</a><a href="#">WHEN YOU NEED US</a><a href="#">WHERE TO REACH US</a>
  </nav>
</header>

<section class="hero" role="img" aria-label="Photo of a data center aisle lined with illuminated server racks">
  <div class="hero-tag">15th year of hosting<br>without a <strong>single hosting</strong><br>without any downtime</div>
  <div class="dots"><span></span><span class="on"></span><span></span><span></span><span></span></div>
</section>

<section class="plans">
  <div class="wrap">
    <h2 class="section-title">HOSTING PLANS</h2>
    <div class="section-rule"></div>
    <div class="plan-row">
      <div class="plan"><h3>WEB HOSTING</h3><p>It is a long established fact that a</p><div class="price"><small>STARTING AT</small><div>$ 65<span> / MO</span></div></div><a class="btn">GET STARTED &nbsp;»</a></div>
      <div class="plan"><h3>VPS HOSTING</h3><p>It is a long established fact that a</p><div class="price"><small>STARTING AT</small><div>$ 85<span> / MO</span></div></div><a class="btn">GET STARTED &nbsp;»</a></div>
      <div class="plan"><h3>WINDOWS HOSTING</h3><p>It is a long established fact that a</p><div class="price"><small>STARTING AT</small><div>$ 110<span> / MO</span></div></div><a class="btn">GET STARTED &nbsp;»</a></div>
    </div>
  </div>
</section>

<section class="features">
  <div class="wrap">
    <h2 class="section-title">WHAT WE DO</h2>
    <div class="section-rule"></div>
    <div class="feature-grid">
      <div class="feature"><svg width="48" height="48" viewBox="0 0 48 48" fill="none" stroke="#2f86cf" stroke-width="3"><path d="M40 24a16 16 0 11-6-12.5"/><path d="M36 8v5h-5"/><text x="24" y="29" font-size="13" font-family="Montserrat" font-weight="700" fill="#2f86cf" stroke="none" text-anchor="middle">24</text></svg><h4>24/7 LIVE SUPPORT</h4><p>There are many variations of passages of Lorem Ipsum available but the majority have suffered</p></div>
      <div class="feature"><svg width="56" height="48" viewBox="0 0 56 48" fill="none" stroke="#2f86cf" stroke-width="3"><circle cx="20" cy="28" r="11" stroke-dasharray="5 3"/><circle cx="20" cy="28" r="4"/><circle cx="41" cy="12" r="7" stroke-dasharray="4 2"/><circle cx="41" cy="12" r="2"/></svg><h4>ADMIN CONTROLS</h4><p>There are many variations of passages of Lorem Ipsum available but the majority have suffered</p></div>
      <div class="feature"><svg width="48" height="48" viewBox="0 0 48 48" fill="none" stroke="#2f86cf" stroke-width="3"><circle cx="24" cy="24" r="19"/><path d="M24 24l8-10"/><circle cx="24" cy="24" r="2" fill="#2f86cf"/></svg><h4>HIGH PERFORMANCE</h4><p>There are many variations of passages of Lorem Ipsum available but the majority have suffered</p></div>
      <div class="feature"><svg width="48" height="48" viewBox="0 0 48 48" fill="none" stroke="#2f86cf" stroke-width="3"><rect x="10" y="21" width="28" height="22" rx="2"/><path d="M16 21v-6a8 8 0 0116 0v6"/><path d="M24 29v6"/></svg><h4>PRIVACY COMPLIANCE</h4><p>There are many variations of passages of Lorem Ipsum available but the majority have suffered</p></div>
      <div class="feature"><svg width="52" height="48" viewBox="0 0 52 48" fill="none" stroke="#2f86cf" stroke-width="3"><path d="M22 4l16 6v12c0 10-7 17-16 21C13 39 6 32 6 22V10z"/><circle cx="37" cy="35" r="9" fill="#2f86cf"/><path d="M33 35l3 3 5-6" stroke="#fff"/></svg><h4>ADVANCED SECURITY</h4><p>There are many variations of passages of Lorem Ipsum available but the majority have suffered</p></div>
      <div class="feature"><svg width="48" height="48" viewBox="0 0 48 48" fill="none" stroke="#2f86cf" stroke-width="4" stroke-linecap="round"><path d="M8 40L30 18"/><path d="M28 10a8 8 0 0010 10"/><path d="M10 8l30 32"/><path d="M6 12l6-6"/></svg><h4>INFRASTRUCTURE</h4><p>There are many variations of passages of Lorem Ipsum available but the majority have suffered</p></div>
    </div>
  </div>
</section>

<section class="why">
  <div class="wrap">
    <h2 class="section-title">WHY FERRO WAVE</h2>
    <div class="section-rule"></div>
    <div class="why-grid">
      <div class="why-item"><svg width="96" height="64" viewBox="0 0 96 64"><g transform="rotate(-18 48 32)" fill="none" stroke="#2f86cf" stroke-width="3"><rect x="14" y="14" width="64" height="34" rx="3" fill="#2f86cf"/><rect x="20" y="20" width="52" height="22" stroke="#fff"/><circle cx="46" cy="31" r="8" fill="#fff" stroke="none"/><text x="46" y="36" font-size="13" font-family="Montserrat" font-weight="700" fill="#2f86cf" stroke="none" text-anchor="middle">$</text></g></svg><h4>30 DAYS GUARANTEE</h4><p>There are many variations of passages of Lorem Ipsum available but the majority have suffered</p></div>
      <div class="why-item"><svg width="64" height="64" viewBox="0 0 64 64" fill="none" stroke="#2f86cf" stroke-width="3"><rect x="8" y="6" width="40" height="14" rx="2" fill="#2f86cf"/><rect x="8" y="24" width="40" height="14" rx="2" fill="#2f86cf"/><path d="M14 13h14M14 31h14" stroke="#fff"/><path d="M46 62V44M38 52l8-8 8 8"/></svg><h4>99.9% UPTIME</h4><p>There are many variations of passages of Lorem Ipsum available but the majority have suffered</p></div>
      <div class="why-item"><svg width="64" height="64" viewBox="0 0 64 64" fill="none" stroke="#2f86cf" stroke-width="3"><rect x="14" y="2" width="36" height="12" rx="2"/><rect x="14" y="17" width="36" height="12" rx="2"/><rect x="14" y="32" width="36" height="12" rx="2"/><path d="M20 8h4M20 23h4M20 38h4M32 44v10M8 56h48"/><circle cx="32" cy="56" r="3" fill="#2f86cf"/></svg><h4>DEDICATED SERVERS</h4><p>There are many variations of passages of Lorem Ipsum available but the majority have suffered</p></div>
    </div>
  </div>
</section>

<section class="advisors">
  <div class="wrap">
    <h2 class="section-title">SMALL COMPANIES ADVISOR</h2>
    <div class="section-rule"></div>
    <svg class="arrow" style="left:-16px" width="14" height="26" viewBox="0 0 14 26"><path d="M12 2L2 13l10 11" stroke="#a9adb3" stroke-width="2.5" fill="none"/></svg>
    <svg class="arrow" style="right:-16px" width="14" height="26" viewBox="0 0 14 26"><path d="M2 2l10 11L2 24" stroke="#a9adb3" stroke-width="2.5" fill="none"/></svg>
    <div class="advisor-row">
      <div class="advisor"><div class="photo" role="img" aria-label="Portrait photo of a smiling businesswoman" style="background:linear-gradient(180deg,#d9d6d2,#b7a9a0)"></div><div><h4>IT IS A LONG ESTABLISHED FACT A READER WILL BE DISTRAC</h4><p>There are many variations of passages of Lorem Ipsum available, but the majority have suffered alteration.</p><a href="#">VIEW MORE</a></div></div>
      <div class="advisor"><div class="photo" role="img" aria-label="Portrait photo of a smiling businessman" style="background:linear-gradient(180deg,#7b6a5e,#c9c3bd)"></div><div><h4>IT IS A LONG ESTABLISHED FACT A READER WILL BE DISTRAC</h4><p>There are many variations of passages of Lorem Ipsum available, but the majority have suffered alteration.</p><a href="#">VIEW MORE</a></div></div>
    </div>
  </div>
</section>

<section class="reach">
  <div class="wrap">
    <div class="follow"><b>FOLLOW US</b><span style="background:#2f4f8f"></span><span style="background:#3aa2e0"></span><span style="background:#e1552f"></span><span style="background:#1f76b3"></span></div>
    <div class="contacts">
      <div class="contact"><span class="ring" style="width:40px;height:40px"><svg width="12" height="16" viewBox="0 0 12 16"><path fill="#2f86cf" d="M6 0a6 6 0 00-6 6c0 4.5 6 10 6 10s6-5.5 6-10a6 6 0 00-6-6zm0 8.2A2.2 2.2 0 116 3.8a2.2 2.2 0 010 4.4z"/></svg></span><div class="addr">4819 E. Tolliver Bend #317,<br>Holloway Ridge, AR 72190</div></div>
      <div class="contact"><span class="ring" style="width:40px;height:40px"><svg width="14" height="10" viewBox="0 0 14 10"><rect width="14" height="10" rx="1" fill="#2f86cf"/><path d="M0 1l7 5 7-5" stroke="#fff" fill="none"/></svg></span><div><small>Email</small>myferrowave@mailnest.example</div></div>
      <div class="contact"><span class="ring" style="width:40px;height:40px"><svg width="14" height="14" viewBox="0 0 24 24"><path fill="#2f86cf" d="M6.6 10.8a15 15 0 006.6 6.6l2.2-2.2c.3-.3.7-.4 1-.2 1.1.4 2.3.6 3.6.6.6 0 1 .4 1 1V20c0 .6-.4 1-1 1A17 17 0 013 4c0-.6.4-1 1-1h3.5c.6 0 1 .4 1 1 0 1.3.2 2.5.6 3.6.1.3 0 .7-.2 1z"/></svg></span><div><small>CALL</small><span style="font-size:15px">888.514.2973</span></div></div>
    </div>
  </div>
</section>

<footer class="site-footer">
  <div class="wrap">
    <div class="footer-brand"><span class="brand-mark"></span><span class="brand-name">FERRO WAVE</span></div>
    <div class="footer-cols">
      <div><h5>MENU</h5><ul><li>Home</li><li>Who we are</li><li>What we do</li><li>When you need us</li><li>Where to reach us</li></ul></div>
      <div><h5>HOSTING</h5><ul><li>Shared Hosting</li><li>Windows Hosting</li><li>VPS Hosting</li><li>Managed Server</li><li>Dedicated Server</li><li>Business Email</li></ul></div>
      <div><h5>SUPPORT</h5><ul><li>Customer Portal</li><li>Support Portal</li><li>Payment Options</li><li>Forums</li></ul></div>
    </div>
  </div>
</footer>

<div class="bottom-bar">
  <div class="wrap"><span>Sitemap &nbsp;|&nbsp; Legal &nbsp;|&nbsp; Privacy Policy</span><span>Copyrights @ 2017 All Rights Reserved</span></div>
</div>

</body>
</html>
```